Catholic composer needs poster for new musical, "THE STONE AND THE VIGIL, the Harvest Musical"

We need a dynamic poster for "The Stone and the Vigil," a new musical written for Catholic dinner theater. We need you to create an iconic design like you see in posters for classic musicals, like "Rosa Calendula," Lantern of the Harbour," or "Gilded." In our musical, “fire” represents the Holy Spirit, who showers man with his merciful love.

Miraculous events occur. A mighty wind from heaven fills the house. Tongues of fire appear over their heads. They speak in other tongues that are understandable by all present. They are emboldened to go out and tell the Good News to the world, despite the risks associated with evangelizing this fledgling religion. They exclaim, “Lord, you will show us the path to life.”

Target Market(s)

The audience is adult members of Catholic churches. But don't make the design look too "churchy."

Requirements
Must have
• Photoshop or Illustrated file with layers, or vector format.
Should not have
• Really don't want photos.

```html
<!DOCTYPE html>
<html lang="en">
<head>
<meta charset="utf-8">
<title>The Stone and the Vigil – The Harvest Musical</title>
<link rel="stylesheet" href="https://fonts.googleapis.com/css2?family=Libre+Baskerville:ital,wght@0,400;0,700;1,400;1,700&display=swap">
<style>
  :root {
    --ember: #c8300e;
    --flame: #f58a16;
    --gold: #ffd93a;
    --ice: #2f8fe0;
    --deep-ice: #0a3a86;
    --figure-core: #3a2422;
    --crimson: #a3131a;
    --title-red: #8d1015;
    --ink: #1c1310;
    --ticket-yellow: #ffe84a;
    --ticket-red: #c92018;
    --paper: #fff7e6;
  }
  * { margin: 0; padding: 0; box-sizing: border-box; }
  html, body { width: 849px; height: 1200px; overflow: hidden; background: #ffffff; }
  .poster {
    position: relative;
    width: 849px;
    height: 1200px;
    overflow: hidden;
    font-family: "Libre Baskerville", "Times New Roman", serif;
    color: var(--ink);
  }
  .elements-backdrop {
    position: absolute;
    inset: 0;
    background:
      radial-gradient(ellipse 40% 22% at 50% 82%, rgba(255,250,238,0.97), rgba(255,250,238,0) 100%),
      radial-gradient(ellipse 35% 18% at 22% 4%, rgba(255,226,70,0.95), rgba(255,226,70,0) 100%),
      radial-gradient(ellipse 30% 18% at 78% 4%, rgba(120,210,90,0.7), rgba(120,210,90,0) 100%),
      radial-gradient(ellipse 22% 40% at 8% 55%, rgba(150,20,5,0.8), rgba(150,20,5,0) 100%),
      radial-gradient(ellipse 22% 40% at 94% 55%, rgba(5,30,100,0.8), rgba(5,30,100,0) 100%),
      linear-gradient(90deg, var(--ember) 0%, var(--flame) 22%, var(--gold) 40%, #fff1cf 50%, #9fd0f6 60%, var(--ice) 78%, var(--deep-ice) 100%);
  }
  .figure-art {
    position: absolute;
    left: 130px;
    top: 150px;
    width: 590px;
    height: 560px;
    border-radius: 50% 50% 40% 40% / 38% 38% 62% 62%;
    background:
      radial-gradient(ellipse 18% 22% at 50% 30%, rgba(40,24,22,0.85), rgba(40,24,22,0) 100%),
      linear-gradient(90deg, rgba(30,10,5,0) 0%, rgba(30,10,5,0.65) 12%, rgba(255,215,120,0.9) 32%, rgba(250,240,215,0.95) 49%, rgba(190,225,255,0.95) 51%, rgba(120,180,240,0.9) 68%, rgba(5,20,60,0.65) 88%, rgba(5,20,60,0) 100%);
    filter: blur(6px);
  }
  .rule {
    position: absolute;
    left: 99px;
    width: 665px;
    height: 3px;
    background: var(--crimson);
  }
  .rule.top { top: 700px; }
  .rule.bottom { top: 790px; }
  .show-title {
    position: absolute;
    left: 0; right: 0;
    top: 716px;
    text-align: center;
    font-size: 40px;
    font-weight: 700;
    color: var(--title-red);
    text-shadow: 2px 2px 0 #f4d59a, 3px 3px 4px rgba(0,0,0,0.35);
    line-height: 44px;
  }
  .show-subtitle {
    position: absolute;
    left: 0; right: 0;
    top: 756px;
    text-align: center;
    font-size: 28px;
    font-style: italic;
    color: var(--title-red);
    line-height: 30px;
  }
  .show-tagline {
    position: absolute;
    left: 0; right: 0;
    top: 824px;
    text-align: center;
    font-size: 23px;
    font-weight: 700;
    line-height: 30px;
    color: var(--ink);
  }
  .show-quote {
    position: absolute;
    left: 0; right: 0;
    top: 898px;
    text-align: center;
    font-size: 40px;
    font-weight: 700;
    line-height: 50px;
    color: var(--crimson);
  }
  .event-details {
    position: absolute;
    left: 212px;
    top: 1013px;
    width: 440px;
    height: 102px;
    padding: 6px 0 0 16px;
    background: var(--ticket-yellow);
    font-size: 22px;
    line-height: 30px;
    color: var(--crimson);
    list-style: none;
  }
  .site-address {
    position: absolute;
    left: 270px;
    top: 1144px;
    width: 310px;
    height: 28px;
    background: rgba(255,247,230,0.85);
    text-align: center;
    font-size: 15px;
    line-height: 28px;
    color: var(--crimson);
  }
  .ticket-price {
    position: absolute;
    left: 10px;
    top: 1052px;
    width: 92px;
    text-align: center;
    color: var(--ticket-red);
  }
  .ticket-price .label {
    display: block;
    font-size: 22px;
    font-style: italic;
    line-height: 30px;
    color: var(--gold);
  }
  .ticket-price .amount {
    display: block;
    margin-top: 4px;
    height: 90px;
    background: var(--ticket-yellow);
    font-size: 32px;
    font-weight: 700;
    line-height: 90px;
  }
</style>
</head>
<body>
  <main class="poster">
    <div class="elements-backdrop"></div>
    <div class="figure-art" role="img" aria-label="Painted figure with long flowing hair and outstretched arms at the centre, one half wrapped in roaring orange flames, the other in swirling blue water"></div>

    <span class="rule top"></span>
    <h1 class="show-title">THE STONE AND THE VIGIL</h1>
    <p class="show-subtitle">The Harvest Musical</p>
    <span class="rule bottom"></span>

    <p class="show-tagline">A new musical for Catholic Dinner Theater<br>By Ray Lindqvist</p>

    <p class="show-quote">“O Spirit come,<br>You are merciful love”</p>

    <ul class="event-details">
      <li>Where:</li>
      <li>Date:</li>
      <li>Time:</li>
    </ul>

    <p class="site-address">www.thestoneandthevigil.com</p>

    <div class="ticket-price">
      <span class="label">Ticket</span>
      <span class="amount">$50</span>
    </div>
  </main>
</body>
</html>
```